Rooted Ready Rising: Quiet Roots, Open Doors, Steady Hands

I want a modern and clean looking book cover. 5.25x8

Title
Rooted Ready Rising

Subtitle
Quiet Roots, Open Doors, Steady Hands

I don’t just want a graphic, I want it to make sense. If it can just be the words and a textured looking background, I’ll be ok with that too. I just want it to look crisp, clean, modern.

I want the back to have my book blurb and bio attached with the pic that’s attached.

Target Market(s)

Self help

Requirements
Must have
• Modern, clean look, look professional, attract customers.

```html
<!DOCTYPE html>
<html lang="en">
<head>
<meta charset="utf-8">
<title>Rooted Ready Rising: Quiet Roots, Open Doors, Steady Hands</title>
<link rel="stylesheet" href="https://fonts.googleapis.com/css2?family=Alfa+Slab+One&family=Lato:ital,wght@0,700;1,900&display=swap">
<style>
  :root {
    --cover-pink: #e30f6a;
    --ink-black: #000000;
    --paper-white: #ffffff;
    --shadow-maroon: #5e0627;
  }
  html, body {
    margin: 0;
    padding: 0;
    width: 788px;
    height: 1200px;
    overflow: hidden;
    background: var(--cover-pink);
  }
  .cover {
    position: relative;
    width: 788px;
    height: 1200px;
    overflow: hidden;
    background: var(--cover-pink);
    font-family: "Lato", "Helvetica Neue", Arial, sans-serif;
  }
  .cover-grain {
    position: absolute;
    inset: 0;
    width: 100%;
    height: 100%;
    opacity: 0.22;
    mix-blend-mode: multiply;
  }
  .subtitle {
    position: absolute;
    top: 38px;
    left: 0;
    width: 100%;
    margin: 0;
    text-align: center;
    color: var(--paper-white);
    font-weight: 700;
    font-size: 28px;
    line-height: 36px;
    letter-spacing: 0.11em;
    text-transform: uppercase;
  }
  .monogram {
    position: absolute;
    left: 232px;
    top: 147px;
    width: 330px;
    height: 906px;
  }
  .monogram text {
    font-family: "Alfa Slab One", "Rockwell", serif;
    fill: var(--ink-black);
  }
  .title {
    position: absolute;
    top: 262px;
    left: 0;
    width: 100%;
    margin: 0;
    text-align: center;
    color: var(--paper-white);
    font-style: italic;
    font-weight: 900;
    text-transform: uppercase;
    letter-spacing: -0.01em;
    text-shadow: 7px 7px 0 var(--shadow-maroon);
  }
  .title-word {
    display: block;
    line-height: 1;
  }
  .title-word--rooted { font-size: 150px; margin-bottom: 50px; }
  .title-word--ready  { font-size: 188px; margin-bottom: 26px; }
  .title-word--rising { font-size: 182px; }
  .author {
    position: absolute;
    bottom: 38px;
    left: 0;
    width: 100%;
    margin: 0;
    text-align: center;
    color: var(--paper-white);
    font-weight: 700;
    font-size: 48px;
    letter-spacing: 0.1em;
    text-transform: uppercase;
  }
</style>
</head>
<body>
<main class="cover">
  <svg class="cover-grain" viewBox="0 0 788 1200" preserveAspectRatio="none" aria-hidden="true">
    <filter id="grain-filter">
      <feTurbulence type="fractalNoise" baseFrequency="0.9" numOctaves="2" stitchTiles="stitch"/>
      <feColorMatrix type="saturate" values="0"/>
    </filter>
    <rect width="788" height="1200" filter="url(#grain-filter)"/>
  </svg>

  <p class="subtitle">Quiet Roots, Open Doors,<br>Steady Hands</p>

  <svg class="monogram" viewBox="0 -72 70 72" preserveAspectRatio="none" aria-hidden="true">
    <text x="0" y="0" font-size="100" textLength="70" lengthAdjust="spacingAndGlyphs">R</text>
  </svg>

  <h1 class="title">
    <span class="title-word title-word--rooted">Rooted</span>
    <span class="title-word title-word--ready">Ready</span>
    <span class="title-word title-word--rising">Rising</span>
  </h1>

  <p class="author">Author Name</p>
</main>
</body>
</html>
```